Assessment Service for Aged Care clients information booklet

Our organisation, the Brindle Vale District Review Bureau, provides in home assessments to aged clients who are seeking assistance with everyday tasks that will support them to remain living in their home. We need a booklet designed to provide to our clients following an aged care assessment for in home services.
Target Market(s)
Aged people living in the community
Industry/Entity Type
Seeking
Colors
Designer to choose colors to be used in the design.
Requirements
Must have
- The booklet must have large print (minimum 12 font size) and be easy to read by the aging consumer. Should be A4 sized. As the content changes from time to time, we need the ability to edit the text. Photos of independent seniors
Nice to have
- reflect the interests of community living seniors
Should not have
- Bright colours that make it difficult to read. Background art under text. Commonwealth Government Logo. Photos of frail aged people (no wheelchairs, carers, anything that make a person look dependent)

```html
<!DOCTYPE html>
<html lang="en">
<head>
<meta charset="utf-8">
<title>Brindle Vale District Review Bureau – Client Information Booklet</title>
<link href="https://fonts.googleapis.com/css2?family=Questrial&family=Open+Sans:wght@400;700&display=swap" rel="stylesheet">
<style>
:root{
  --backdrop:#2a2a2a;
  --paper:#ffffff;
  --ink:#333333;
  --muted:#777777;
  --heading:#2f5e9a;
  --label:#2a5595;
  --strip:#dcefe9;
  --rule:#9fd3cf;
  --table-head:#dcefe6;
  --table-line:#9aa8a6;
  --field-line:#c9cfd0;
  --accent-warm:rgba(251,243,180,.75);
  --accent-cool:rgba(200,230,223,.75);
}
*{box-sizing:border-box;margin:0;padding:0}
html,body{width:1200px;height:1200px;overflow:hidden;background:var(--backdrop)}
.stage{position:absolute;left:0;top:0;width:1500px;height:1500px;transform:scale(.8);transform-origin:0 0;font-family:"Open Sans",Verdana,sans-serif;color:var(--ink)}
.spread,.single{position:absolute;background:var(--paper);box-shadow:0 2px 8px rgba(0,0,0,.35)}
.spread-feedback{left:133px;top:108px;width:745px;height:526px}
.spread-resources{left:668px;top:530px;width:745px;height:526px}
.single-cover{left:133px;top:704px;width:496px;height:701px;overflow:hidden}
.fold{position:absolute;top:0;bottom:0;width:1px;background:#444}
.edge-strip{position:absolute;left:0;top:0;bottom:0;width:22px;background:var(--strip)}
.abs{position:absolute}
.page-title{font-family:"Questrial",sans-serif;font-weight:400;color:var(--heading);font-size:18px;line-height:22px}
.body-text{font-size:7.8px;line-height:10px;letter-spacing:.12px}
.body-text p{margin-bottom:10px}
.org-name{color:var(--label);font-weight:700}
.region{color:var(--label);font-style:italic}
.photo{position:absolute}
.accent{position:absolute;border-radius:50%;background:radial-gradient(circle at 40% 35%,var(--accent-warm) 0%,var(--accent-cool) 55%,rgba(255,255,255,0) 72%)}
.page-num{font-size:7.6px}
.resource{border-bottom:1px solid var(--rule);padding-bottom:8px;margin-bottom:8px}
.resource:last-child{border-bottom:0}
.bullet-cols{display:flex;margin:10px 0 8px}
.bullets{list-style:none;width:148px}
.bullets li{position:relative;padding-left:7px;margin-bottom:5px}
.bullets li::before{content:"";position:absolute;left:0;top:4px;width:3px;height:3px;border-radius:50%;background:var(--heading)}
.bullets.tight li{margin-bottom:0}
.field-line{position:absolute;height:1px;background:var(--field-line)}
.notes-line{position:absolute;left:1074px;width:282px;height:1px;background:var(--field-line)}
.referral-table{position:absolute;left:1074px;top:903px;width:282px;border-collapse:collapse;font-size:6.8px}
.referral-table th{background:var(--table-head);font-weight:400;text-align:left;padding:0 6px;height:24px;border:1px solid var(--table-line)}
.referral-table td{height:26.5px;border:1px solid var(--table-line)}
.small-label{font-family:"Questrial",sans-serif;font-size:7px;color:var(--muted)}
</style>
</head>
<body>
<div class="stage">

  <section class="spread spread-feedback">
    <div class="edge-strip"></div>
    <div class="fold" style="left:372px"></div>

    <div class="photo" role="img" aria-label="Photo of an independent older woman smiling while using a laptop at home" style="left:70px;top:24px;width:113px;height:80px;background:linear-gradient(135deg,#e9e6e2 0%,#d8cfc4 45%,#b98a4a 75%,#8f6b3e 100%)"></div>

    <h2 class="page-title abs" style="left:70px;top:116px">How to Provide Feedback</h2>
    <div class="body-text abs" style="left:70px;top:146px;width:245px">
      <p>In the first instance, we encourage you to provide feedback to the Assessment organisation who undertook the assessment.</p>
      <p>A feedback form and envelope has been left for you. You can use this form or contact the Bureau directly to offer your feedback.</p>
      <p>If you are not satisfied with the response you have received from the Bureau, you may contact the following agencies:</p>
      <p style="margin-top:14px"><span class="org-name">Northvale State Health &amp; Community Office</span><br>The Northvale State Health &amp; Community Office is responsible to manage the Brindle Vale District Review Bureau in Northvale on behalf of the National office until 30 June 2019. You can contact the nearest Northvale Health &amp; Community Divisional Office:</p>
      <p><span class="org-name">Health and Community Office</span><br><span class="region">Western Region</span><br>14 Carrow Lane Elmsford, Northvale 3921<br>1300 555 014<br>Web: https://www.nshco.example.org</p>
      <p><span class="org-name">Senior Care Complaints Ombudsman (National)</span><br>You may also choose to contact the Senior Care Complaints Ombudsman on the details below:</p>
      <p>PO Box 4120, Harbourton NV 3000<br>Phone: 1800 555 730<br>Web: https://www.seniorcarecomplaints.example.org/</p>
    </div>
    <div class="page-num abs" style="left:182px;top:503px">12</div>

    <div class="accent" role="img" aria-label="Soft pastel decorative accent" style="left:676px;top:14px;width:60px;height:70px"></div>
    <h2 class="page-title abs" style="left:461px;top:116px">Who to Contact if Your<br>Needs Change</h2>
    <div class="body-text abs" style="left:461px;top:170px;width:198px">
      <p>After your Home Support Assessment you may be referred to a service provider to help you to meet your needs. If you require any changes to this service call the service provider directly.</p>
      <p>If your health or needs change significantly or you need a change to your current support plan you can request a review or a new assessment with the Elder Care Connect Review Bureau. To organise a review or new assessment you can call Elder Care Connect 1800 555 281 or the Brindle Vale District Review Bureau who completed your last assessment.</p>
    </div>
    <div class="photo" role="img" aria-label="Photo of a group of active older friends sharing a meal outdoors among cypress trees" style="left:462px;top:305px;width:194px;height:132px;background:linear-gradient(180deg,#c9d6c2 0%,#8ea07a 35%,#6f7d5a 60%,#b4a895 85%,#7d6a55 100%)"></div>
  </section>

  <section class="single single-cover">
    <div class="accent" role="img" aria-label="Soft pastel decorative accent" style="left:330px;top:30px;width:140px;height:172px"></div>
    <div class="photo" role="img" aria-label="Photo of an older couple walking arm in arm barefoot along a sunny beach" style="left:0;top:290px;width:496px;height:411px;background:linear-gradient(180deg,rgba(255,255,255,1) 0%,#f4f1ea 40%,#e7e2d8 62%,#d8cfc0 80%,#cbbfad 100%)"></div>
  </section>

  <section class="spread spread-resources">
    <div class="edge-strip"></div>
    <div class="fold" style="left:373px"></div>

    <div class="photo" role="img" aria-label="Photo of a grandparent playing with a grandchild on a swing in a garden" style="left:222px;top:30px;width:118px;height:80px;background:linear-gradient(135deg,#6f8a4e 0%,#a7b47c 40%,#d8d2b6 60%,#7b9a55 100%)"></div>
    <h2 class="page-title abs" style="left:48px;top:74px">Other Helpful<br>Resources</h2>
    <div class="body-text abs" style="left:49px;top:124px;width:290px">
      <div class="resource">
        <span class="org-name">Elder Rights Northvale</span><br>Elder Rights Northvale provides information, support, advice and education to help prevent elder abuse and help safeguard the rights, dignity and independence of older people. Their services include:
        <div class="bullet-cols" style="margin-top:18px">
          <ul class="bullets tight"><li>Helpline</li><li>Short term support and advocacy for individuals</li></ul>
          <ul class="bullets tight"><li>Free Specialist Legal Services</li><li>Community education</li></ul>
        </div>
        Phone: 1300 555 642<br>Web: https://elderrights.example.org/
      </div>
      <div class="resource">
        <span class="org-name">Future Care Planning Advisory Service</span><br>The Future Care planning advisory service provides support and Advice for Future Care planning. Future care planning lets other people know in advance your wishes about healthcare if you ever become too unwell to make decisions or speak for yourself.<br><br>
        Phone: 1300 555 319<br>Web: https://www.futurecareplanning.example.org
      </div>
      <div class="resource">
        <span class="org-name">Seniors Information Northvale</span><br>Seniors Information Northvale offers free information as an independent service, supported by the state government, on a wide range of issues of interest to older Northvale residents including:
        <div class="bullet-cols">
          <ul class="bullets"><li>Housing options from independent living to residential care</li><li>Concessions and Pensions</li><li>Home-based and community services</li></ul>
          <ul class="bullets"><li>General information on financial and legal issues</li><li>Health and wellbeing</li><li>Retirement</li><li>New learning opportunities, and much more</li></ul>
        </div>
        Phone: 1300 555 908
      </div>
    </div>
    <div class="page-num abs" style="left:182px;top:503px">14</div>

    <div class="accent" role="img" aria-label="Soft pastel decorative accent" style="left:642px;top:38px;width:80px;height:100px"></div>
    <h2 class="page-title abs" style="left:406px;top:34px">Information and Contacts</h2>
    <div class="small-label abs" style="left:406px;top:60px;line-height:11px">If you wish to contact your Assessor or Elder Care Connect<br>the details are listed below.</div>
    <div class="small-label abs" style="left:406px;top:92px">Bureau</div>
    <div class="field-line" style="left:406px;top:114px;width:56px"></div>
    <div class="small-label abs" style="left:518px;top:92px">Elder Care Connect</div>
    <div class="body-text abs" style="left:518px;top:106px">1800 555 281</div>
    <div class="body-text abs" style="left:406px;top:136px">The name of the Assessor visiting you today is:</div>
    <div class="field-line" style="left:406px;top:164px;width:196px"></div>
    <div class="body-text abs" style="left:406px;top:186px">Your Elder Care number is: AC</div>
    <div class="field-line" style="left:532px;top:194px;width:72px"></div>
    <div class="body-text abs" style="left:406px;top:216px">What we discussed today?</div>
  </section>

  <div class="notes-line" style="top:769px"></div>
  <div class="notes-line" style="top:784px"></div>
  <div class="notes-line" style="top:799px"></div>
  <div class="notes-line" style="top:814px"></div>
  <div class="notes-line" style="top:829px"></div>
  <div class="notes-line" style="top:844px"></div>
  <div class="notes-line" style="top:859px"></div>
  <div class="notes-line" style="top:874px"></div>

  <div class="body-text org-name abs" style="left:1074px;top:886px">Services You Will Be Referred For:</div>
  <table class="referral-table">
    <thead><tr><th style="width:131px">Service Type</th><th>Provider(s) Requested or Referral Code</th></tr></thead>
    <tbody>
      <tr><td></td><td></td></tr>
      <tr><td></td><td></td></tr>
      <tr><td></td><td></td></tr>
      <tr><td></td><td></td></tr>
    </tbody>
  </table>

</div>
</body>
</html>
```